Start up needs juice bottle label design

Bramblecrest Citrus Co juice company needs juice bottle label design for all natural lemonades, teas, smoothies and cold-pressed juice. We would like the design to have a space for multiple flavors or custom recipes for special orders. Below is the company logo.

Target Market(s)

On-the-go Health conscious

```html
<!DOCTYPE html>
<html lang="en">
<head>
<meta charset="UTF-8">
<title>Bramblecrest Citrus Co – Cold Pressed Juice Label</title>
<link href="https://fonts.googleapis.com/css2?family=Anton&family=Oswald:wght@300;600&family=Josefin+Sans:wght@700&family=Montserrat:ital,wght@0,500;0,700;0,800;1,300&display=swap" rel="stylesheet">
<style>
  :root {
    --backdrop: #d6cfca;
    --label-orange: #ec8328;
    --label-orange-deep: #e06f14;
    --ink-white: #ffffff;
    --brand-cyan: #3ec8f0;
  }
  html, body {
    margin: 0;
    padding: 0;
    width: 1200px;
    height: 1130px;
    overflow: hidden;
    background: var(--backdrop);
  }
  .canvas {
    position: relative;
    width: 1200px;
    height: 1130px;
  }
  .label {
    position: absolute;
    left: 439px;
    top: 200px;
    width: 318px;
    height: 820px;
    border-radius: 56px 56px 26px 26px;
    background: linear-gradient(90deg, var(--label-orange-deep) 0%, var(--label-orange) 50%, var(--label-orange-deep) 100%);
    color: var(--ink-white);
    text-align: center;
  }
  .label > * {
    position: absolute;
    left: 0;
    right: 0;
    margin: 0 auto;
  }
  .brand-name {
    top: 163px;
    font-family: "Montserrat", sans-serif;
    font-weight: 800;
    font-size: 30px;
    line-height: 1.1;
    color: var(--brand-cyan);
  }
  .title-cold {
    top: 284px;
    font-family: "Anton", sans-serif;
    font-size: 91px;
    line-height: 1;
    letter-spacing: 2px;
    transform: scaleX(1.06);
  }
  .title-pressed {
    top: 382px;
    width: 152px;
    height: 48px;
    box-sizing: border-box;
    border: 3px solid var(--ink-white);
    font-family: "Oswald", sans-serif;
    font-weight: 600;
    font-size: 35px;
    line-height: 40px;
  }
  .title-juice {
    top: 436px;
    font-family: "Anton", sans-serif;
    font-size: 65px;
    line-height: 1;
    letter-spacing: 2px;
    transform: scaleX(1.4);
  }
  .rule {
    background: var(--ink-white);
    width: 208px;
  }
  .rule--top { top: 512px; height: 6px; }
  .rule--short { top: 587px; height: 3px; width: 102px; }
  .rule--mid { top: 658px; height: 6px; }
  .rule--thin { top: 707px; height: 2px; }
  .flavor-name {
    top: 526px;
    font-family: "Josefin Sans", sans-serif;
    font-weight: 700;
    font-size: 27px;
    line-height: 1.1;
  }
  .flavor-fruits {
    top: 553px;
    font-family: "Montserrat", sans-serif;
    font-style: italic;
    font-weight: 300;
    font-size: 17px;
    line-height: 1.2;
    word-spacing: 5px;
  }
  .blend-note {
    top: 594px;
    width: 220px;
    font-family: "Oswald", sans-serif;
    font-weight: 300;
    font-size: 21px;
    line-height: 30px;
  }
  .warning {
    top: 669px;
    width: 208px;
    font-family: "Montserrat", sans-serif;
    font-weight: 500;
    font-size: 7.1px;
    line-height: 8.4px;
    text-align: left;
  }
  .volume {
    top: 761px;
    left: 63px;
    right: auto;
    font-family: "Montserrat", sans-serif;
    font-weight: 700;
    font-size: 15.5px;
    letter-spacing: 0.3px;
  }
  .badge {
    top: 721px;
    left: 190px;
    right: auto;
    width: 64px;
    height: 64px;
  }
</style>
</head>
<body>
<div class="canvas">
  <section class="label">
    <h1 class="brand-name">Bramblecrest<br>Citrus Co</h1>
    <div class="title-cold">COLD</div>
    <div class="title-pressed">PRESSED</div>
    <div class="title-juice">JUICE</div>
    <div class="rule rule--top"></div>
    <div class="flavor-name">Sunset Drift</div>
    <div class="flavor-fruits">orange banana mango</div>
    <div class="rule rule--short"></div>
    <div class="blend-note">100% Vegetable and Fruit<br>Juice Blend</div>
    <div class="rule rule--mid"></div>
    <p class="warning">WARNING: This product has not been pasteurized and therefore may contain harmful bacteria that can cause serious illness in children, the elderly, and persons with weakened immune systems.</p>
    <div class="rule rule--thin"></div>
    <div class="volume">16oz/473ml</div>
    <svg class="badge" viewBox="0 0 64 64" role="img" aria-label="Certification badge">
      <circle cx="32" cy="32" r="29" fill="none" stroke="rgba(255,255,255,0.6)" stroke-width="2"/>
    </svg>
  </section>
</div>
</body>
</html>
```